Brookvane Counsel Partners Website Design

I need a website design for my new business consulting and executive coaching firm, Brookvane Counsel Partners. We provide consultative services to business C-suites as well as personal coaching to executives. I have attached the logo with color scheme I have chosen. I would like the website to reflect professionalism and continue the color scheme in the logo.

Target Market(s)

Small to medium business and their executives; middle to upper income men and women in mid- to late career looking for significance

Industry/Entity Type

Business Consultant

Number of Pages Required

4 page

Requirements
Must have
• A homepage with prominent logo and way to contact for more information; an area on the homepage with easy to read, clear text to describe what the company does; a prominent area on the homepage for a tagline; a blog page that can be updated regularly, an "about us" page with biographical information; an "about us" page; a page detailing services offered
• The web design must match the logo colors and font that I have uploaded.
Nice to have
• A lighthouse picture in the background or header
Should not have
• A lot of text area on the homepage

```html
<!DOCTYPE html>
<html lang="en">
<head>
<meta charset="utf-8">
<title>Brookvane Counsel Partners</title>
<link href="https://fonts.googleapis.com/css2?family=Raleway:wght@400;500;600;700&family=Lato:wght@400;700&display=swap" rel="stylesheet">
<style>
:root{
  --maroon:#7a1212;
  --navy:#1d2b52;
  --ink:#2a2a2a;
  --body:#3c3c3c;
  --hero-a:#f1f1f1;
  --hero-b:#e4e6ea;
  --panel:rgba(236,236,238,0.82);
  --deep-a:#061326;
  --deep-b:#0d3564;
  --card:#f4f4f4;
  --white:#ffffff;
}
*{margin:0;padding:0;box-sizing:border-box}
html,body{width:1200px;height:1200px;overflow:hidden}
body{position:relative;background:var(--white);font-family:'Lato',sans-serif;color:var(--body)}
.abs{position:absolute}

.hero{left:0;top:0;width:1200px;height:670px;background:linear-gradient(180deg,var(--hero-a),var(--hero-b) 70%,#e9ecf1)}
.hero-photo{left:0;top:0;width:560px;height:620px;background:radial-gradient(ellipse at 45% 35%,#e8e8e8 0%,#d9d9d9 45%,rgba(228,230,234,0) 75%)}
.headline{left:611px;top:50px;width:520px;font-family:'Raleway',sans-serif;font-weight:700;font-size:31px;line-height:32.5px;color:var(--maroon)}
.intro{left:611px;width:455px;font-family:'Raleway',sans-serif;font-size:12px;line-height:16px;color:var(--ink)}

.services{left:150px;top:334px;width:900px;height:248px;background:var(--panel)}
.svc-icon{width:56px;height:56px}
.svc-title{font-family:'Raleway',sans-serif;font-weight:600;font-size:13.6px;color:var(--ink)}
.svc-text{width:205px;font-size:9.8px;line-height:13.5px;color:var(--body)}

.btn{left:536px;top:598px;width:128px;height:35px;border:2px solid var(--navy);font-family:'Raleway',sans-serif;font-weight:700;font-size:10.5px;color:var(--navy);display:flex;align-items:center;justify-content:center;letter-spacing:0.2px}

.band{left:0;top:670px;width:1200px;height:406px;background:linear-gradient(100deg,var(--deep-a) 0%,var(--deep-b) 50%,var(--deep-a) 100%)}
.card{width:375px;height:331px;top:709px;background:var(--card)}
.card-photo{left:0;top:0;width:375px;height:160px}
.card-title{left:23px;top:176px;font-family:'Raleway',sans-serif;font-weight:600;font-size:17.6px;color:var(--maroon)}
.card-text{left:23px;width:340px;font-size:9.9px;line-height:13.5px;color:var(--body)}

.feeds{left:0;top:1076px;width:1200px;height:124px;background:linear-gradient(180deg,#f4f4f4,#fafafa)}
.feed-title{top:1124px;font-family:'Raleway',sans-serif;font-size:24px;color:var(--maroon)}
.feed-rule{top:1156px;width:26px;height:2px;background:var(--maroon)}
.feed-photo{top:1171px;height:29px;border:1px solid #d8d8d8}
.tweet{left:511px;top:1178px;width:200px;font-size:9px;line-height:12px;color:var(--body)}
.tweet .handle{color:#3d8fd1}
</style>
</head>
<body>

<section class="abs hero">
  <div class="abs hero-photo" role="img" aria-label="Photo of a thoughtful executive in glasses working at a laptop in a bright office"></div>
  <h1 class="abs headline">Attackers employ new methods every day.<br>It is time for you to step up your game.</h1>
  <p class="abs intro" style="top:194px">Lorem ipsum dolor sit amet, consectetur adipisicing elit, sed do eiusmod tempor incididunt ut labore et dolore magna aliqua. Ut enim ad minim veniam, quis nostrud exercitation ullamco laboris nisi ut aliquip ex ea commodo consequat.</p>
  <p class="abs intro" style="top:257px">Duis aute irure dolor in reprehenderit in voluptate velit esse cillum dolore eu fugiat nulla pariatur. Excepteur sint occaecat cupidatat non proident, sunt in culpa qui officia deserunt mollit anim id est laborum.</p>
</section>

<section class="abs services">
  <!-- Consultative Services -->
  <svg class="abs svc-icon" style="left:10px;top:22px" viewBox="0 0 56 56">
    <circle cx="24" cy="14" r="10" fill="var(--navy)"/>
    <path d="M4 52 Q4 30 24 28 Q44 30 44 52 Z" fill="var(--navy)"/>
    <circle cx="43" cy="44" r="8" fill="var(--navy)" stroke="#eee" stroke-width="2"/>
    <circle cx="42" cy="43" r="3.5" fill="none" stroke="#fff" stroke-width="1.8"/>
    <line x1="44.5" y1="45.5" x2="47.5" y2="48.5" stroke="#fff" stroke-width="1.8"/>
  </svg>
  <div class="abs svc-title" style="left:86px;top:20px">Consultative Services</div>
  <p class="abs svc-text" style="left:86px;top:52px">Nam vel eleifend que fusce consequat pretium velit vitae. Vulputate nullam pharetra lorem laoreet. Etiam sollicitudin magna nullam.</p>

  <!-- Executive Coaching -->
  <svg class="abs svc-icon" style="left:310px;top:20px" viewBox="0 0 56 56">
    <path d="M12 44 Q3 44 3 36 Q3 28 12 28 Q13 18 24 17 Q33 10 41 20 Q53 20 53 32 Q53 44 42 44 Z" fill="none" stroke="var(--navy)" stroke-width="3"/>
  </svg>
  <div class="abs svc-title" style="left:386px;top:20px">Executive Coaching</div>
  <p class="abs svc-text" style="left:386px;top:52px">Nam vel eleifend que fusce consequat pretium velit vitae. Vulputate nullam pharetra lorem laoreet. Etiam sollicitudin magna nullam.</p>

  <!-- Fresh & Right Ideas -->
  <svg class="abs svc-icon" style="left:614px;top:22px" viewBox="0 0 56 56">
    <path d="M28 3 Q46 3 46 20 Q46 29 38 37 L36 44 L20 44 L18 37 Q10 29 10 20 Q10 3 28 3 Z" fill="none" stroke="var(--navy)" stroke-width="3"/>
    <path d="M20 12 Q24 8 29 9" fill="none" stroke="var(--navy)" stroke-width="2"/>
    <line x1="21" y1="49" x2="35" y2="49" stroke="var(--navy)" stroke-width="3"/>
    <line x1="24" y1="54" x2="32" y2="54" stroke="var(--navy)" stroke-width="3"/>
  </svg>
  <div class="abs svc-title" style="left:686px;top:20px">Fresh &amp; Right Ideas</div>
  <p class="abs svc-text" style="left:686px;top:52px">Nam vel eleifend que fusce consequat pretium velit vitae. Vulputate nullam pharetra lorem laoreet. Etiam sollicitudin magna nullam.</p>

  <!-- Personal Coaching -->
  <svg class="abs svc-icon" style="left:12px;top:150px" viewBox="0 0 56 56">
    <circle cx="28" cy="12" r="10" fill="var(--navy)"/>
    <path d="M8 46 Q8 26 28 25 Q48 26 48 46 Z" fill="var(--navy)"/>
    <circle cx="10" cy="43" r="6" fill="var(--navy)" stroke="#eee" stroke-width="2"/>
    <circle cx="48" cy="45" r="6" fill="var(--navy)" stroke="#eee" stroke-width="2"/>
    <line x1="4" y1="22" x2="8" y2="38" stroke="var(--navy)" stroke-width="2"/>
  </svg>
  <div class="abs svc-title" style="left:86px;top:150px">Personal Coaching</div>
  <p class="abs svc-text" style="left:86px;top:182px">Nam vel eleifend que fusce consequat pretium velit vitae. Vulputate nullam pharetra lorem laoreet. Etiam sollicitudin magna nullam.</p>

  <!-- Business Consulting -->
  <svg class="abs svc-icon" style="left:310px;top:148px" viewBox="0 0 56 56">
    <rect x="2" y="12" width="38" height="32" rx="4" fill="none" stroke="var(--navy)" stroke-width="3"/>
    <rect x="10" y="19" width="22" height="18" rx="2" fill="var(--navy)"/>
    <path d="M40 22 L53 13 L53 43 L40 34 Z" fill="none" stroke="var(--navy)" stroke-width="3" stroke-linejoin="round"/>
  </svg>
  <div class="abs svc-title" style="left:386px;top:150px">Business Consulting</div>
  <p class="abs svc-text" style="left:386px;top:182px">Nam vel eleifend que fusce consequat pretium velit vitae. Vulputate nullam pharetra lorem laoreet. Etiam sollicitudin magna nullam.</p>
</section>

<a class="abs btn">VIEW ALL SERVICES</a>

<section class="abs band" role="img" aria-label="Dark blue backdrop of illuminated server racks"></section>

<article class="abs card" style="left:214px">
  <div class="abs card-photo" role="img" aria-label="Hands holding a tablet showing a blue stock chart" style="background:linear-gradient(90deg,#8a8d90,#2a3440 40%,#1d5a9c 60%,#3a3d42)"></div>
  <h2 class="abs card-title">Request a Demo</h2>
  <p class="abs card-text" style="top:206px">Lorem ipsum dolor sit amet, consectetur adipisicing elit, sed do eiusmod tempor incididunt ut labore et dolore magna aliqua. Ut enim ad minim veniam, quis nostrud exercitation ullamco laboris nisi ut aliquip ex ea commodo consequat.</p>
  <p class="abs card-text" style="top:274px">Duis aute irure dolor in reprehenderit in voluptate velit esse cillum dolore eu fugiat nulla pariatur. Excepteur sint occaecat cupidatat non proident, sunt in culpa qui officia deserunt mollit anim id est laborum.</p>
</article>

<article class="abs card" style="left:611px">
  <div class="abs card-photo" role="img" aria-label="Operations center with analysts at monitors beneath a wall of screens" style="background:linear-gradient(180deg,#2b2f38 0%,#4b5566 45%,#c9ccd2 75%,#e2e3e6)"></div>
  <h2 class="abs card-title">Success Stories</h2>
  <p class="abs card-text" style="top:206px">Ut enim ad minim veniam, quis nostrud exercitation ullamco laboris nisi ut aliquip ex ea commodo consequat.  Duis aute irure dolor in reprehenderit in voluptate velit esse cillum dolore eu fugiat nulla pariatur.</p>
  <p class="abs card-text" style="top:260px">Excepteur sint occaecat cupidatat non proident, sunt in culpa qui officia deserunt mollit anim id est laborum. Sed ut perspiciatis unde omnis iste natus error sit voluptatem accusantium doloremque laudantium, totam rem aperiam, eaque ipsa quae ab illo inventore veritatis.</p>
</article>

<section class="abs feeds"></section>

<h3 class="abs feed-title" style="left:213px">Press Releases</h3>
<div class="abs feed-rule" style="left:213px"></div>
<div class="abs feed-photo" style="left:213px;width:249px;background:linear-gradient(90deg,#3a6f8a,#c9d6dc 60%,#b88f7a)" role="img" aria-label="Press release photo of hands signing a document"></div>

<h3 class="abs feed-title" style="left:472px">Latest Tweets</h3>
<div class="abs feed-rule" style="left:472px"></div>
<svg class="abs" style="left:487px;top:1178px;width:14px;height:14px" viewBox="0 0 14 14">
  <path d="M7 1.5 Q13 1.5 13 6 Q13 10.5 7 10.5 L4 12.5 L4.5 9.8 Q1 8.8 1 6 Q1 1.5 7 1.5 Z" fill="none" stroke="#3d8fd1" stroke-width="1.6"/>
</svg>
<p class="abs tweet">Most inspiring meeting ever! RT <span class="handle">@DanielMarsh</span> Amazing meeting with the</p>

<h3 class="abs feed-title" style="left:737px">Executive Blog</h3>
<div class="abs feed-rule" style="left:737px"></div>
<div class="abs feed-photo" style="left:737px;width:249px;background:linear-gradient(90deg,#dfe3e8,#8a9ab0 50%,#e8e2dc)" role="img" aria-label="Blog photo of executives in a meeting"></div>

</body>
</html>
```